***Rustic Website Design - More design needed after!***

Tindlebrook Creative Agency
https://www.picturelane.example/tindlebrookco/

Website pages:
Home
About
Design
-Logo Design and Branding
-Graphic Design
Websites
-Hosting, Maintenance and Support
Social Media
Managed Marketing
Portfolio
Contact

I have included a link to our Picturelane so you get a feel as to how we want to be.

We want to be approachable to new and rural businesses. - Colours included as image

Target Market(s)

Start Up Businesses & Rural Businesses

Number of Pages Required

2 page

Font styles to use
Serif
Other font styles liked:
• Barnyard, Rustic

Requirements
Must have
• Menu, Social Media Icons, rustic lines like our social media.

```html
<!DOCTYPE html>
<html lang="en">
<head>
<meta charset="utf-8">
<title>Tindlebrook Creative Agency</title>
<link rel="stylesheet" href="https://fonts.googleapis.com/css2?family=Kurale&family=Open+Sans:wght@400;600&family=Allura&display=swap">
<style>
:root{
  --teal:#0c4f4a;
  --teal-soft:#4f8a84;
  --yellow:#f9cc25;
  --cream:#fcf8ec;
  --maroon:#74213a;
  --paper:#f4f2ef;
  --ink:#5a5a5a;
  --white:#ffffff;
}
*{margin:0;padding:0;box-sizing:border-box}
html,body{width:955px;height:1200px;overflow:hidden}
body{position:relative;background:var(--white);font-family:'Open Sans',sans-serif}
.abs{position:absolute}
.hero-band{left:0;top:0;width:955px;height:382px;background:var(--teal)}
.hero-cream{left:0;top:382px;width:955px;height:225px;background:var(--cream)}
.about-bg{left:0;top:607px;width:955px;height:593px;background:linear-gradient(#fff 0,#fff 90px,var(--paper) 200px,var(--paper) 440px,var(--cream) 450px)}
.brand{left:42px;top:0;width:117px;height:116px;background:var(--teal);box-shadow:0 4px 12px rgba(0,0,0,.25);display:flex;align-items:center;justify-content:center;text-align:center;font-family:'Kurale',serif;color:var(--white);font-size:19px;line-height:1.05}
.nav-mark{left:230px;top:0;width:46px;height:2px;background:var(--yellow)}
.nav{top:52px;left:0;height:28px;font-family:'Kurale',serif;font-size:14.5px;color:var(--yellow);line-height:28px;white-space:nowrap}
.nav.home{color:var(--white)}
.nav-contact{left:819px;top:52px;width:88px;height:28px;background:var(--yellow);color:var(--teal);font-family:'Kurale',serif;font-size:14.5px;text-align:center;line-height:28px;box-shadow:0 4px 10px rgba(0,0,0,.2)}
.photo{left:41px;top:187px;width:324px;height:353px;background:linear-gradient(135deg,#d9d3c8,#b08a6a 55%,#8a6a52);}
.hero-title{left:455px;top:180px;font-family:'Kurale',serif;font-size:48px;line-height:56px;color:var(--white);text-shadow:0 3px 6px rgba(0,0,0,.25)}
.hero-title .accent{color:var(--yellow)}
.hero-lead{left:455px;top:305px;width:330px;font-size:17px;line-height:19px;color:var(--teal-soft)}
.hero-cta{left:454px;top:364px;width:182px;height:39px;background:var(--yellow);color:var(--teal);font-weight:600;font-size:16px;text-align:center;line-height:39px;box-shadow:0 8px 14px rgba(0,0,0,.18)}
.client{top:455px;width:74px;height:48px;border-radius:6px;background:#2a2a2a}
.client.round{border-radius:50%;width:58px;height:58px;top:450px}
.about-script{left:0;width:955px;top:628px;text-align:center;font-family:'Allura',cursive;font-size:44px;color:var(--yellow)}
.about-title{left:0;width:955px;top:674px;text-align:center;font-family:'Kurale',serif;font-size:33px;color:var(--teal)}
.about-rule{left:466px;top:736px;width:60px;height:3px;background:var(--teal)}
.about-text{left:237px;top:758px;width:530px;text-align:center;font-size:10.5px;line-height:16.5px;color:var(--ink)}
.card{top:891px;width:217px;height:279px;background:var(--maroon);box-shadow:0 10px 20px rgba(0,0,0,.18);text-align:center;color:var(--white)}
.card .notch{position:absolute;width:28px;height:28px;border-radius:50%;background:var(--paper)}
.card .notch.b{background:var(--cream)}
.card .notch::after{content:"";position:absolute;width:10px;height:10px;border-radius:50%;background:var(--yellow);left:9px;top:9px}
.card .badge{position:absolute;left:61px;top:-47px;width:95px;height:95px;border-radius:50%;background:var(--yellow);display:flex;align-items:center;justify-content:center}
.card h3{position:absolute;left:0;width:217px;top:58px;font-family:'Kurale',serif;font-weight:400;font-size:23px;color:var(--yellow)}
.card .rule{position:absolute;left:71px;top:102px;width:75px;height:3px;background:var(--yellow)}
.card p{position:absolute;left:22px;top:117px;width:173px;font-size:10.5px;line-height:16.5px}
.card .more{position:absolute;left:63px;top:231px;width:88px;height:28px;background:var(--yellow);color:var(--maroon);font-family:'Kurale',serif;font-size:14.5px;line-height:28px}
</style>
</head>
<body>
<div class="abs hero-band"></div>
<div class="abs hero-cream"></div>
<div class="abs about-bg"></div>

<div class="abs brand">Tindlebrook</div>
<div class="abs nav-mark"></div>
<div class="abs nav home" style="left:235px">Home</div>
<div class="abs nav" style="left:296px">About</div>
<div class="abs nav" style="left:359px">Design</div>
<div class="abs nav" style="left:427px">Websites</div>
<div class="abs nav" style="left:505px">Social Media</div>
<div class="abs nav" style="left:607px">Managed Marketing</div>
<div class="abs nav" style="left:749px">Portfolio</div>
<div class="abs nav-contact">Contact</div>

<svg class="abs" style="left:0;top:160px" width="420" height="400" viewBox="0 0 420 400">
  <path d="M0 300 C40 260 80 200 110 150 C150 60 200 10 260 12 C330 15 400 120 413 230 C420 320 330 395 240 395 C170 400 90 390 40 370 C10 360 0 340 0 300Z" fill="var(--yellow)"/>
</svg>
<div class="abs photo" role="img" aria-label="Photo of four smiling colleagues gathered around a laptop"></div>

<div class="abs hero-title">Digital <span class="accent">Growth</span><br>Specialists</div>
<div class="abs hero-lead">Unlock your next opportunity with our range of digital marketing services.</div>
<div class="abs hero-cta">Get In Touch</div>

<div class="abs client" style="left:457px"></div>
<div class="abs client" style="left:550px"></div>
<div class="abs client" style="left:646px"></div>
<div class="abs client" style="left:742px"></div>
<div class="abs client round" style="left:846px"></div>

<div class="abs about-script">ABOUT US</div>
<div class="abs about-title">Making growth potential a reality</div>
<div class="abs about-rule"></div>
<div class="abs about-text">Lorem Ipsum is simply dummy text of the printing and typesetting industry. Lorem Ipsum has been the industry's standard dummy text ever since the 1500s, when an unknown printer took a galley of type and scrambled it to make a type specimen book.</div>

<div class="abs card" style="left:101px">
  <span class="notch" style="left:-14px;top:-14px"></span><span class="notch" style="right:-14px;top:-14px"></span>
  <span class="notch b" style="left:-14px;bottom:-14px"></span><span class="notch b" style="right:-14px;bottom:-14px"></span>
  <div class="badge"><svg width="48" height="58" viewBox="0 0 48 58" fill="none" stroke="#1c1c1c" stroke-width="2"><path d="M14 44 L16 30 C10 28 8 22 12 18 L22 12 L22 4 L28 9 C38 12 40 26 36 44Z"/><path d="M8 50 H40 M6 55 H42 M10 44 H38"/><circle cx="24" cy="18" r="1.5" fill="#1c1c1c"/></svg></div>
  <h3>Digital Strategy</h3><div class="rule"></div>
  <p>Lorem Ipsum is simply dummy text of the printing and typesetting industry. Lorem Ipsum has been the industry's standard dummy text ever since the 1500s,</p>
  <div class="more">Learn More</div>
</div>

<div class="abs card" style="left:366px">
  <span class="notch" style="left:-14px;top:-14px"></span><span class="notch" style="right:-14px;top:-14px"></span>
  <span class="notch b" style="left:-14px;bottom:-14px"></span><span class="notch b" style="right:-14px;bottom:-14px"></span>
  <div class="badge"><svg width="52" height="52" viewBox="0 0 52 52" fill="none" stroke="#1c1c1c" stroke-width="2"><rect x="16" y="2" width="24" height="44"/><rect x="2" y="22" width="18" height="26"/><rect x="30" y="30" width="20" height="18"/><path d="M21 9 H35 M21 15 H35 M6 30 H16 M6 38 H16 M34 36 H46 M34 42 H46 M11 26 V48 M40 30 V48"/></svg></div>
  <h3>Web Development</h3><div class="rule"></div>
  <p>Lorem Ipsum is simply dummy text of the printing and typesetting industry. Lorem Ipsum has been the industry's standard dummy text ever since the 1500s,</p>
  <div class="more">Learn More</div>
</div>

<div class="abs card" style="left:632px">
  <span class="notch" style="left:-14px;top:-14px"></span><span class="notch" style="right:-14px;top:-14px"></span>
  <span class="notch b" style="left:-14px;bottom:-14px"></span><span class="notch b" style="right:-14px;bottom:-14px"></span>
  <div class="badge"><svg width="48" height="58" viewBox="0 0 48 58" fill="none" stroke="#1c1c1c" stroke-width="2"><path d="M14 44 L16 30 C10 28 8 22 12 18 L22 12 L22 4 L28 9 C38 12 40 26 36 44Z"/><path d="M8 50 H40 M6 55 H42 M10 44 H38"/><circle cx="24" cy="18" r="1.5" fill="#1c1c1c"/></svg></div>
  <h3>Digital Marketing</h3><div class="rule"></div>
  <p>Lorem Ipsum is simply dummy text of the printing and typesetting industry. Lorem Ipsum has been the industry's standard dummy text ever since the 1500s,</p>
  <div class="more">Learn More</div>
</div>
</body>
</html>
```